Business Card For Kelmora Financial Consulting

Hi, I would like a business card designed. Bold, modern.
Please use the same design as the logo. I have also attached the website design to see the overall theme.
Wordmark Font
Color: Hex: #01AEF7

```html
<!DOCTYPE html>
<html lang="en">
<head>
<meta charset="utf-8">
<title>Kelmora Financial Consulting – Business Card</title>
<link rel="stylesheet" href="https://fonts.googleapis.com/css2?family=Poppins:wght@400;500;600;700&display=swap">
<style>
  :root {
    --stage: #76757a;
    --card: #17212b;
    --card-edge: #0f171f;
    --brand-blue: #01aef7;
    --ink-white: #f2f5f8;
    --ink-soft: #c9d2da;
  }
  * { box-sizing: border-box; margin: 0; padding: 0; }
  html, body {
    width: 1200px; height: 900px; overflow: hidden;
    background: var(--stage);
    font-family: "Poppins", sans-serif;
  }
  .stage {
    position: relative; width: 1200px; height: 900px;
    display: flex; flex-direction: column; align-items: center; justify-content: center; gap: 40px;
  }
  .card {
    position: relative; width: 700px; height: 400px;
    background: var(--card);
    box-shadow: 0 10px 24px rgba(0,0,0,.35);
    border-bottom: 3px solid var(--card-edge);
    overflow: hidden;
  }

  /* shared brand name */
  .brand { display: flex; align-items: center; gap: 14px; }
  .brand-square { width: 30px; height: 30px; border: 3px solid var(--brand-blue); }
  .brand-name {
    font-weight: 600; color: var(--ink-white);
    letter-spacing: .08em; text-transform: uppercase; line-height: 1;
  }

  /* front */
  .card-front .brand { position: absolute; left: 44px; top: 52px; }
  .card-front .brand-name { font-size: 22px; }
  .divider {
    position: absolute; left: 300px; right: 0; top: 238px;
    height: 1px; background: var(--brand-blue);
  }
  .person { position: absolute; left: 44px; top: 214px; }
  .person-name { font-size: 22px; font-weight: 700; color: var(--ink-white); letter-spacing: .03em; line-height: 1.1; }
  .person-role { font-size: 13px; font-weight: 500; color: var(--brand-blue); letter-spacing: .04em; margin-top: 4px; }
  .contact-list { list-style: none; margin-top: 18px; }
  .contact-list li {
    display: flex; align-items: center; gap: 12px;
    font-size: 14px; color: var(--ink-soft); height: 26px;
  }
  .icon-box {
    width: 18px; height: 18px; border: 1.5px solid var(--brand-blue);
    display: flex; align-items: center; justify-content: center;
  }
  .icon-box svg { width: 11px; height: 11px; }
  .address {
    position: absolute; left: 420px; top: 262px;
    display: flex; gap: 12px; align-items: flex-start;
  }
  .address p { font-size: 14px; line-height: 1.5; color: var(--ink-soft); }

  /* back */
  .card-back .brand { position: absolute; left: 50%; top: 150px; transform: translateX(-50%); gap: 20px; }
  .card-back .brand-square { width: 48px; height: 48px; border-width: 4px; }
  .card-back .brand-name { font-size: 40px; }
  .web-address {
    position: absolute; left: 0; right: 0; top: 300px; text-align: center;
    font-size: 16px; color: var(--ink-white); letter-spacing: .14em;
  }
</style>
</head>
<body>
<main class="stage">

  <section class="card card-front" aria-label="Business card front">
    <div class="brand">
      <span class="brand-square"></span>
      <span class="brand-name">Kelmora Consulting</span>
    </div>

    <div class="divider"></div>

    <div class="person">
      <h1 class="person-name">DANIEL HARPER</h1>
      <p class="person-role">MANAGING DIRECTOR</p>
      <ul class="contact-list">
        <li>
          <span class="icon-box"><svg viewBox="0 0 12 12"><path d="M2.5 1.5l2 2-1 1.2a6 6 0 0 0 3.8 3.8l1.2-1 2 2-1.3 1.3C5 10.5 1.5 7 1.2 2.8z" fill="none" stroke="#01aef7" stroke-width="1.1"/></svg></span>
          214-555-0187
        </li>
        <li>
          <span class="icon-box"><svg viewBox="0 0 12 12"><rect x="1" y="2.5" width="10" height="7" fill="none" stroke="#01aef7" stroke-width="1.1"/><path d="M1 2.5l5 4 5-4" fill="none" stroke="#01aef7" stroke-width="1.1"/></svg></span>
          daniel@kelmora.com
        </li>
        <li>
          <span class="icon-box"><svg viewBox="0 0 12 12"><circle cx="6" cy="6" r="4.7" fill="none" stroke="#01aef7" stroke-width="1.1"/><ellipse cx="6" cy="6" rx="2" ry="4.7" fill="none" stroke="#01aef7" stroke-width="1"/><path d="M1.3 6h9.4" stroke="#01aef7" stroke-width="1"/></svg></span>
          www.kelmoraconsulting.com
        </li>
      </ul>
    </div>

    <div class="address">
      <span class="icon-box"><svg viewBox="0 0 12 12"><path d="M6 11S2.5 7.3 2.5 4.8a3.5 3.5 0 0 1 7 0C9.5 7.3 6 11 6 11z" fill="none" stroke="#01aef7" stroke-width="1.1"/><circle cx="6" cy="4.8" r="1.2" fill="#01aef7"/></svg></span>
      <p>418 Fulton Street West<br>Suite 200, Grand Rapids<br>MI 49504</p>
    </div>
  </section>

  <section class="card card-back" aria-label="Business card back">
    <div class="brand">
      <span class="brand-square"></span>
      <span class="brand-name">Kelmora Consulting</span>
    </div>
    <p class="web-address">WWW.KELMORACONSULTING.COM</p>
  </section>

</main>
</body>
</html>
```